Conference banner for Beacon training organisation

We empower everyday heroes.
We provide training that empowers individuals to create positive change in themselves, their community, and the world.
We need a large banner design to promote the organisation at conferences and events. We are open to ideas and creativity.
It may involve creatively displaying our logo only, or it may involve our logo and a summary of our products (Beacon training, Steady Minds Crisis Care).
Size: 820mm width x 1790mm height
300dpi
Target Market(s)
Educators and frontline health, community, and social workers.
Industry/Entity Type
Training
Colors
Designer to choose colors to be used in the design.

```html
<!DOCTYPE html>
<html lang="en">
<head>
<meta charset="utf-8">
<title>Beacon Training – Conference Banner</title>
<link rel="stylesheet" href="https://fonts.googleapis.com/css2?family=Oswald:wght@400;500;600&display=swap">
<style>
  :root {
    --brand-red: #c2414f;
    --brand-red-deep: #8f2a37;
    --brand-blue: #4b5ea9;
    --brand-blue-deep: #2f3b79;
    --paper: #ffffff;
  }
  html, body {
    margin: 0;
    padding: 0;
    width: 1200px;
    height: 2620px;
    overflow: hidden;
    background: var(--paper);
  }
  .banner {
    position: relative;
    width: 1200px;
    height: 2620px;
    overflow: hidden;
    background: var(--paper);
    font-family: "Oswald", "Arial Narrow", sans-serif;
  }
  .ribbons {
    position: absolute;
    inset: 0;
    width: 1200px;
    height: 2620px;
  }
  .ribbon-red { fill: var(--brand-red); }
  .ribbon-blue { fill: var(--brand-blue); }
  .ribbon-shadow { fill: var(--brand-blue-deep); }
  .ribbon-shadow-red { fill: var(--brand-red-deep); }

  .corner-brand {
    position: absolute;
    top: 52px;
    right: 52px;
    display: flex;
    flex-direction: column;
    align-items: center;
    gap: 10px;
    color: var(--paper);
    font-weight: 600;
    font-size: 40px;
    letter-spacing: 2px;
    line-height: 1;
  }
  .corner-brand .brand-dot {
    width: 34px;
    height: 34px;
    border-radius: 50%;
    background: var(--paper);
  }

  .hero-brand {
    position: absolute;
    left: 170px;
    top: 470px;
    width: 560px;
    display: flex;
    flex-direction: column;
    align-items: center;
    gap: 36px;
  }
  .hero-brand .brand-dot {
    width: 150px;
    height: 150px;
    border-radius: 50%;
    background: var(--brand-blue);
  }
  .hero-brand .brand-name {
    color: var(--brand-red);
    font-weight: 600;
    font-size: 150px;
    line-height: 0.95;
    letter-spacing: 6px;
    text-align: center;
  }

  .headline {
    position: absolute;
    inset: 0;
    margin: 0;
    font-weight: 400;
  }
  .outline-word {
    position: absolute;
    left: 70px;
    font-size: 340px;
    line-height: 1;
    letter-spacing: 4px;
    white-space: nowrap;
  }
  .outline-word.row-top { top: 1250px; }
  .outline-word.row-bottom { top: 1580px; }
  .outline-word .layer {
    position: absolute;
    left: 0;
    top: 0;
    color: transparent;
    -webkit-text-stroke: 6px var(--brand-blue);
  }
  .outline-word .layer-back {
    -webkit-text-stroke: 6px var(--brand-red);
    transform: translate(12px, 9px);
  }
  .solid-word {
    position: absolute;
    left: 625px;
    color: var(--brand-blue);
    font-weight: 500;
    font-size: 150px;
    line-height: 1;
    letter-spacing: 4px;
    white-space: nowrap;
  }
  .solid-word.line-one { top: 1610px; }
  .solid-word.line-two { top: 1770px; }
</style>
</head>
<body>
<main class="banner">
  <svg class="ribbons" viewBox="0 0 1200 2620" aria-hidden="true">
    <polygon class="ribbon-red" points="640,0 1200,0 1200,380"/>
    <polygon class="ribbon-blue" points="560,0 640,0 1200,380 1200,440"/>
    <polygon class="ribbon-blue" points="1060,480 1200,440 1200,560 1000,1300 880,1250"/>
    <polygon class="ribbon-shadow" points="880,1250 1000,1300 940,1330"/>
    <polygon class="ribbon-red" points="1200,560 1200,1600 1010,1380 1000,1300"/>
    <polygon class="ribbon-blue" points="1200,1560 1200,1720 860,2280 760,2200"/>
    <polygon class="ribbon-shadow" points="760,2200 860,2280 800,2310"/>
    <polygon class="ribbon-red" points="1200,1720 1200,2180 900,2300 860,2280"/>
    <polygon class="ribbon-blue" points="0,2460 520,2270 560,2400 0,2620"/>
    <polygon class="ribbon-shadow" points="480,2290 640,2480 560,2400"/>
    <polygon class="ribbon-red" points="260,2620 1200,2180 1200,2620"/>
    <polygon class="ribbon-shadow-red" points="900,2300 1200,2180 1200,2230"/>
  </svg>

  <div class="corner-brand">
    <span class="brand-dot"></span>
    <span class="brand-name">BEACON HUB</span>
  </div>

  <div class="hero-brand">
    <span class="brand-dot"></span>
    <span class="brand-name">BEACON<br>HUB</span>
  </div>

  <h1 class="headline" aria-label="Beacon training">
    <span class="outline-word row-top" aria-hidden="true">
      <span class="layer layer-back">BEA</span>
      <span class="layer">BEA</span>
    </span>
    <span class="outline-word row-bottom" aria-hidden="true">
      <span class="layer layer-back">CON</span>
      <span class="layer">CON</span>
    </span>
    <span class="solid-word line-one" aria-hidden="true">TRAI</span>
    <span class="solid-word line-two" aria-hidden="true">NING</span>
  </h1>
</main>
</body>
</html>
```